Tidewell Consulting Schedule Of Rates

We need a brochure / proposal for our new company. Our company is a start up based in Australia who provides engineering and sales support to other renewable energy companies. Our brochure is a pitch-deck / sales item that catalogues our key services. We are engineering consultants.

Our website is www.tidewellpartners.com.au. Please review the website to get a feel of colour schemes etc.

We are looking for a strong, trustworthy feel, but the brochure also needs to be sales driven and to the point.

The second page that contains the $30 price point needs to be loud and clear.

The use of relevant icons throughout the document will be viewed favorably.

Please format the tables to look attractive.

The document will need to be in an editable format so content can be edited by us at a later date.

Please feel free to use the pics within the attached word document. The winning design will be provided with updated, clearer images upon request.

Thank you

Target Market(s)

Businesses that either sell or install solar PV and other renewable energy systems in Australia. Most of target market are likely to be electrical contractors.

Industry/Entity Type

Engineering

Colors
0255a3
0492cd
ffffff

Requirements
Must have
• Icons, graphics presentation, Clean and Clear, Business oriented. Sharp sales feel
Nice to have
• solar picture backgrounds maybe
Should not have
• cartoons, over sales driven,

```html
<!DOCTYPE html>
<html lang="en">
<head>
<meta charset="utf-8">
<title>Tidewell Consulting – Schedule Of Rates</title>
<link rel="stylesheet" href="https://fonts.googleapis.com/css2?family=Open+Sans:wght@300;400;700&display=swap">
<style>
  :root {
    --page-bg: #e9ebee;
    --paper: #ffffff;
    --brand-navy: #0255a3;
    --cover-blue: #0b62a0;
    --brand-sky: #0492cd;
    --title-sky: #3aa8e2;
    --text-soft: #d6e6f3;
    --sub-soft: #a9c9e4;
    --ink: #1b1b1b;
  }
  * { margin: 0; padding: 0; box-sizing: border-box; }
  html, body { width: 1200px; height: 804px; overflow: hidden; }
  body {
    background: var(--page-bg);
    font-family: "Open Sans", Arial, sans-serif;
    position: relative;
  }
  .cover {
    position: absolute;
    left: 338px; top: 32px;
    width: 524px; height: 740px;
    background: var(--paper);
    overflow: hidden;
    box-shadow: 0 6px 24px rgba(0,0,0,.18);
  }
  .brand {
    position: absolute;
    left: 38px; top: 70px;
    display: flex; align-items: center; gap: 8px;
  }
  .brand-mark { width: 12px; height: 12px; background: var(--ink); }
  .brand-name {
    font-weight: 700; font-size: 22px; color: var(--ink); letter-spacing: -0.3px;
  }
  .sky-rule {
    position: absolute; left: 0; top: 150px; width: 100%; height: 6px;
    background: var(--brand-sky);
  }
  .hero-photo {
    position: absolute; left: 0; top: 156px; width: 100%; height: 214px;
    background: linear-gradient(100deg, #4a5a6a 0%, #c98a4a 22%, #e7b06a 30%, #8ea0b2 48%, #5d7f9f 65%, #3d6287 100%);
    clip-path: polygon(0 0, 100% 0, 100% 144px, 0 214px);
  }
  .cover-panel {
    position: absolute; left: 0; top: 0; width: 100%; height: 100%;
  }
  .cover-copy {
    position: absolute; left: 48px; top: 412px;
  }
  .eyebrow {
    font-weight: 300; font-size: 27px; color: var(--text-soft); line-height: 1.2;
  }
  .title {
    font-weight: 700; font-size: 31px; color: var(--title-sky); line-height: 1.3; margin-top: 4px;
  }
  .range {
    font-weight: 300; font-size: 19px; color: var(--sub-soft); margin-top: 4px;
  }
  .web-tab {
    position: absolute; right: 0; bottom: 16px;
    width: 180px; height: 24px; background: var(--paper);
    display: flex; align-items: center; justify-content: center;
    font-size: 9px; color: var(--brand-navy);
  }
</style>
</head>
<body>
  <main class="cover">
    <div class="brand">
      <span class="brand-mark"></span>
      <span class="brand-name">Tidewell Consulting</span>
    </div>

    <div class="sky-rule"></div>
    <div class="hero-photo" role="img" aria-label="Rooftop solar panels at sunset with a city skyline on the horizon"></div>

    <svg class="cover-panel" width="524" height="740" viewBox="0 0 524 740" aria-hidden="true">
      <polygon points="0,370 524,300 524,740 0,740" fill="var(--cover-blue)"/>
      <polygon points="0,156 524,156 524,162 0,178" fill="var(--brand-navy)"/>
      <polygon points="70,170 130,166 102,206" fill="var(--brand-navy)"/>
    </svg>

    <div class="cover-copy">
      <p class="eyebrow">Design &amp; Support Services</p>
      <h1 class="title">Schedule Of Rates</h1>
      <p class="range">Grid and Off Grid 5kW – 10MW</p>
    </div>

    <div class="web-tab">www.tidewellpartners.com.au</div>
  </main>
</body>
</html>
```